Preferred pricing vendor

We are a plumbing company that has many services
-Boilers & Controls
-Plumbing & Heating
-HVAC & Refrigeration
-Preventative Maintenacne
-Gas fitting & Drain Cleaning

We primarily look after condo buildings, and our preferred service rates ($98, $93, or $88 depending on the contract) extend to all of our clients. So in essence, we look after the mechanical room and common equipment but our clients can call us in for drain cleaning or replacing a fixture in their suite. The discounted rates apply to the personal residence. We want a flyer to let them know they get a discount on our services. A one-pager we can send out to all of our contract clients.

Included source files for our letterhead and logo just so you can see the colours we go with.

Target Market(s)

Residential repairs, individual people, replacement of fixtures in-suite specific repairs

Requirements
Must have
• be colourful and attractive

```html
<!DOCTYPE html>
<html lang="en">
<head>
<meta charset="utf-8">
<title>Northbay Mechanical Inc – Preferred Service Rates</title>
<link href="https://fonts.googleapis.com/css2?family=Roboto:wght@400;500;700;900&display=swap" rel="stylesheet">
<style>
  :root {
    --blue: #1f70b8;
    --blue-deep: #1c49a6;
    --blue-light: #8fc1ec;
    --orange: #f05a24;
    --white: #ffffff;
    --ink: #3a3a3a;
  }
  * { box-sizing: border-box; margin: 0; padding: 0; }
  html, body { width: 1008px; height: 1200px; overflow: hidden; background: #f2f2f2; }
  body { font-family: "Roboto", Arial, sans-serif; }
  .flyer { position: relative; width: 1008px; height: 1200px; overflow: hidden; background: var(--blue); }
  .layer { position: absolute; left: 0; top: 0; }

  .brand { position: absolute; left: 0; top: 0; width: 420px; height: 225px;
    display: flex; align-items: center; justify-content: center; gap: 12px; padding-right: 30px; }
  .brand-dot { width: 22px; height: 22px; border-radius: 50%; background: var(--orange); flex: none; }
  .brand-name { color: var(--blue); font-weight: 900; font-size: 30px; line-height: 1.05; text-transform: uppercase; }

  .services { position: absolute; left: 74px; top: 395px; list-style: none; }
  .services li { height: 34px; margin-bottom: 16.5px; background: var(--orange); color: var(--white);
    font-weight: 700; font-size: 20px; line-height: 34px; padding-left: 28px; }

  .call { position: absolute; left: 585px; top: 478px; width: 345px; text-align: center; }
  .call svg { display: block; margin: 0 auto; }
  .call-number { color: var(--blue-light); font-weight: 700; font-size: 54px; letter-spacing: 1px; margin-top: 18px; }

  .headline { position: absolute; left: 94px; top: 688px; color: var(--white); font-weight: 700; font-size: 48px; }

  .rate { position: absolute; left: 96px; width: 282px; height: 60px; }
  .rate-value { position: absolute; left: 74px; top: 0; width: 136px; height: 62px; background: var(--orange);
    border-radius: 9px; color: var(--white); font-weight: 700; font-size: 44px; line-height: 62px; text-align: center; }
  .rate-note { position: absolute; left: 124px; top: 1028px; color: var(--white); font-weight: 700; font-size: 14px; }

  .footer { position: absolute; left: 0; top: 1122px; width: 1008px; height: 78px; background: var(--white);
    display: flex; align-items: center; gap: 34px; padding-left: 36px; color: var(--ink); font-size: 17px; }
  .footer-item { display: flex; align-items: center; gap: 8px; }
  .footer-address { line-height: 1.25; }
</style>
</head>
<body>
<main class="flyer">
  <svg class="layer" width="1008" height="1200" viewBox="0 0 1008 1200">
    <defs>
      <linearGradient id="plantRoom" x1="0" y1="0" x2="1" y2="1">
        <stop offset="0" stop-color="#7d8a9a"/>
        <stop offset="0.45" stop-color="#3e4650"/>
        <stop offset="0.75" stop-color="#d8632c"/>
        <stop offset="1" stop-color="#2f3b48"/>
      </linearGradient>
      <linearGradient id="technician" x1="0" y1="0" x2="1" y2="0">
        <stop offset="0" stop-color="#3a3d42"/>
        <stop offset="0.4" stop-color="#6b7075"/>
        <stop offset="1" stop-color="#9ea3a7"/>
      </linearGradient>
    </defs>
    <rect class="plant-photo" x="0" y="0" width="1008" height="480" fill="url(#plantRoom)" role="img" aria-label="Photo of a mechanical room with orange pipes, pumps and valves"/>
    <polygon class="blue-panel" points="0,476 606,476 650,405 1008,405 1008,1100 0,1100" fill="var(--blue)"/>
    <polygon class="brand-stripe" points="0,225 500,0 532,0 432,236 0,236" fill="var(--orange)"/>
    <polygon class="brand-panel" points="0,0 506,0 410,225 0,225" fill="var(--white)"/>
    <polygon class="tech-frame" points="507,815 1008,797 1008,1100 362,1100" fill="var(--orange)"/>
    <polygon class="tech-photo" points="522,830 1008,818 1008,1100 384,1100" fill="url(#technician)" role="img" aria-label="Photo of a technician in an orange hard hat adjusting a valve"/>
    <polygon class="footer-band" points="0,1088 1008,1094 1008,1125 0,1122" fill="var(--orange)"/>
    <polygon class="rate-ribbon" points="96,835 170,775 378,775 304,835" fill="var(--blue-deep)"/>
    <polygon class="rate-ribbon" points="96,923 170,863 378,863 304,923" fill="var(--blue-deep)"/>
    <polygon class="rate-ribbon" points="96,1005 170,945 378,945 304,1005" fill="var(--blue-deep)"/>
  </svg>

  <div class="brand">
    <span class="brand-dot"></span>
    <span class="brand-name">Northbay<br>Mechanical Inc</span>
  </div>

  <ul class="services">
    <li style="width:292px">Boilers &amp; Controls</li>
    <li style="width:328px">Plumbing &amp; Heating</li>
    <li style="width:366px">HVAC &amp; Refrigeration</li>
    <li style="width:408px">Preventative Maintenacne</li>
    <li style="width:441px">Gas fitting &amp; Drain Cleaning</li>
  </ul>

  <div class="call">
    <svg width="98" height="74" viewBox="0 0 98 74" aria-hidden="true">
      <path d="M4 24 C4 6 94 6 94 24 L94 30 L72 30 L72 20 L26 20 L26 30 L4 30 Z" fill="var(--white)"/>
      <path d="M30 24 L68 24 L88 60 L88 72 L10 72 L10 60 Z" fill="var(--white)"/>
      <g fill="var(--blue)">
        <rect x="38" y="38" width="5" height="5"/><rect x="47" y="38" width="5" height="5"/><rect x="56" y="38" width="5" height="5"/>
        <rect x="38" y="46" width="5" height="5"/><rect x="47" y="46" width="5" height="5"/><rect x="56" y="46" width="5" height="5"/>
        <rect x="38" y="54" width="5" height="5"/><rect x="47" y="54" width="5" height="5"/><rect x="56" y="54" width="5" height="5"/>
      </g>
    </svg>
    <div class="call-number">555.210.4400</div>
  </div>

  <h1 class="headline">Get a discount on our services</h1>

  <div class="rate" style="top:773px"><span class="rate-value">$98</span></div>
  <div class="rate" style="top:861px"><span class="rate-value">$93</span></div>
  <div class="rate" style="top:943px"><span class="rate-value">$88</span></div>
  <p class="rate-note">depending on the contract</p>

  <footer class="footer">
    <div class="footer-item">
      <svg width="18" height="26" viewBox="0 0 18 26" aria-hidden="true"><path d="M9 0 C4 0 0 4 0 9 C0 15 9 26 9 26 C9 26 18 15 18 9 C18 4 14 0 9 0 Z" fill="var(--orange)"/><circle cx="9" cy="9" r="3" fill="var(--white)"/></svg>
      <span class="footer-address">1200 Harbor Crest Avenue,<br>Suite 210 Bayview.</span>
    </div>
    <div class="footer-item">
      <svg width="16" height="12" viewBox="0 0 16 12" aria-hidden="true"><path d="M0 4 C0 0 16 0 16 4 L16 5 L12 5 L12 3 L4 3 L4 5 L0 5 Z M5 4 L11 4 L14 10 L14 12 L2 12 L2 10 Z" fill="var(--orange)"/></svg>
      <span>555.210.4400</span>
    </div>
    <div class="footer-item">
      <svg width="15" height="11" viewBox="0 0 15 11" aria-hidden="true"><rect width="15" height="11" fill="var(--orange)"/><path d="M0 0 L7.5 6 L15 0" stroke="var(--white)" stroke-width="1.4" fill="none"/></svg>
      <span>info@northbaymech.com</span>
    </div>
    <div class="footer-item">
      <svg width="15" height="15" viewBox="0 0 15 15" aria-hidden="true"><circle cx="7.5" cy="7.5" r="7.5" fill="var(--orange)"/><path d="M1 7.5 H14 M7.5 1 C4 4 4 11 7.5 14 M7.5 1 C11 4 11 11 7.5 14" stroke="var(--white)" stroke-width="1" fill="none"/></svg>
      <span>www.northbaymech.com</span>
    </div>
  </footer>
</main>
</body>
</html>
```